Travel Itinerary Planning Website Redesign

We have built our own website for a travel itinerary planning service using Wix but are not professional designers. We need help getting over the finish line with a redesign of our website. <br/><br/>We like material design elements, icons and styling. The pages need to flow well one to another and evoke a sense of exclusivity, without giving the impression that it's unattainable. The website doesn't need to keep its current "boxy" format but instead should have a better aesthetic and flow. We're also looking for a complete redesign of the "How It Works" section (shown on two different pages of the website) to be more visually pleasing and easy to understand (maybe using icons or infographic style people). <br/><br/>We already have our logo and selected colors. The copy is also available on the live site as well. The redesign will focus on 4 pages: the homepage and the three service pages (one page per service). The website is currently live at www.trelmavista.com. Fonts should be Helvetica Bold, Regular and Light. Preferred color scheme is attached.

Target Market(s)

Ages 28-65, living in the US, mostly large cities with a desire for well planned, non-group travels

Industry/Entity Type

Travel Industry

Font styles to use
Other font styles liked:
• Helvetica

Colors

Designer to choose colors to be used in the design.

Requirements
Must have
• Make sure to use colors we provided in the attachment and what's on the current website
• Redesign "How it Works"
• Include ambassadors area
• Have a second page that showcases how the "Personal Trip Planning" page should look
Should not have
• No header menu needed for this project

```html
<!DOCTYPE html>
<html lang="en">
<head>
<meta charset="utf-8">
<title>Trelmavista — Personal Trip Planning</title>
<link href="https://fonts.googleapis.com/css2?family=Oswald:wght@400;500;600&family=Poppins:wght@400;500;600&display=swap" rel="stylesheet">
<style>
:root{
  --sand:#FFD080;
  --lemon:#FDFBB0;
  --brown:#4B3612;
  --footer:#523B1A;
  --footer-field:#6A5230;
  --gold:#C9943A;
  --text:#3a3a3a;
  --muted:#6b6b6b;
  --line:#dcdcdc;
  --white:#ffffff;
}
*{box-sizing:border-box;margin:0;padding:0}
html,body{width:1200px;height:2861px;overflow:hidden}
body{position:relative;background:var(--white);font-family:'Poppins',sans-serif;color:var(--text)}
.abs{position:absolute}
.display{font-family:'Oswald',sans-serif;color:var(--brown);text-transform:uppercase;letter-spacing:-.5px}

/* header */
.site-header{left:0;top:0;width:1200px;height:91px;background:var(--white)}
.brand{left:92px;top:26px;display:flex;align-items:center;gap:10px;font-family:'Oswald',sans-serif;font-weight:600;font-size:26px;color:var(--brown);letter-spacing:.5px}
.brand-dot{width:30px;height:30px;border-radius:50%;background:var(--brown)}
.nav{right:89px;top:38px;display:flex;gap:32px;font-size:13.5px;color:var(--brown)}

/* hero */
.hero{left:0;top:91px;width:1200px;height:429px;background:var(--sand)}
.hero-title{left:88px;top:197px;font-size:62px;line-height:54px;font-weight:600;letter-spacing:-1.5px}
.hero-copy{left:88px;top:324px;width:480px;font-size:14px;line-height:21px;color:#2a2a2a}
.btn{display:inline-flex;align-items:center;justify-content:center;background:var(--white);color:var(--brown);font-weight:500;font-size:13.5px;letter-spacing:.5px;box-shadow:0 4px 10px rgba(0,0,0,.12);border-radius:2px}
.hero-btn{left:89px;top:383px;width:131px;height:45px}
.hero-art{left:589px;top:91px;width:540px;height:429px;background:linear-gradient(180deg,#cfe6ee 0%,#e7d8b4 60%,var(--sand) 100%);clip-path:path('M60 60 Q 40 0 110 0 L 410 0 Q 470 20 480 80 Q 520 160 490 200 L 540 429 L 0 429 Z')}

/* how it works */
.section-title{left:0;width:1200px;text-align:center;font-size:42px;font-weight:500}
.step-title{font-family:'Oswald',sans-serif;font-size:19px;color:var(--brown);text-transform:uppercase;letter-spacing:-.3px}
.step-copy{font-size:14px;line-height:16px;color:var(--muted);margin-top:8px}
.step.left{text-align:right}
.step.right{text-align:left}
.step-icon{width:72px;height:72px;border-radius:50%;background:var(--white);box-shadow:0 6px 16px rgba(0,0,0,.12);display:flex;align-items:center;justify-content:center}
.mascot{left:539px;top:683px;width:122px;height:206px;border-radius:50% 50% 40% 40%;background:linear-gradient(180deg,#d9a95a,var(--brown))}
.divider{left:89px;top:984px;width:1022px;height:1px;background:var(--line)}

/* pricing */
.plan{width:444px;height:455px;box-shadow:0 3px 0 #c8a05a}
.plan.standard{left:149px;top:1225px;background:var(--sand)}
.plan.premium{left:606px;top:1225px;background:var(--lemon)}
.plan-badge{width:138px;height:152px;border-radius:22px;border:5px solid #9ea3a8;background:linear-gradient(180deg,#f2f2ee,#d8d2c0);box-shadow:0 6px 14px rgba(0,0,0,.25)}
.plan-name{position:absolute;top:112px;left:0;width:100%;text-align:center;font-size:27px;font-weight:500}
.plan-price{position:absolute;top:144px;left:0;width:100%;text-align:center;font-family:'Oswald',sans-serif;font-size:18px;color:var(--brown)}
.plan-price b{font-weight:600}
.plan-list{position:absolute;top:186px;left:31px;list-style:none;font-size:14.5px;line-height:26.7px;color:#3d3d3d}
.plan-list li{display:flex;align-items:center;gap:8px}
.plan-list li::before{content:"";width:6px;height:6px;border:2px solid var(--brown);border-radius:50%;flex:none}
.plan-list .lead{font-weight:600;color:var(--brown)}
.plan-btn{position:absolute;top:372px;left:156px;width:131px;height:45px}

/* ambassadors */
.ambassador{width:236px;height:372px;top:1889px;background:var(--white);box-shadow:0 10px 30px rgba(0,0,0,.08);overflow:hidden;border-radius:6px}
.ambassador-photo{position:absolute;top:22px;left:32px;width:250px;height:250px;border-radius:50%;box-shadow:0 10px 0 #ececec}
.ambassador-name{position:absolute;top:308px;left:0;width:100%;text-align:center;font-family:'Oswald',sans-serif;font-size:22px;color:var(--brown);text-transform:uppercase;letter-spacing:-.5px}
.ambassador-role{position:absolute;top:338px;left:0;width:100%;text-align:center;font-size:13.5px;color:var(--gold)}
.dots{left:578px;top:2294px;display:flex;gap:8px}
.dots span{width:10px;height:10px;border-radius:50%;border:1.5px solid #bbb}
.dots span.on{border-color:var(--brown)}

/* footer */
.site-footer{left:0;top:2410px;width:1200px;height:451px;background:var(--footer)}
.footer-mark{left:92px;top:2490px;width:156px;height:200px;border-radius:50% 50% 45% 45%;background:linear-gradient(180deg,#e3b464,#b88a3c)}
.footer-brand{left:92px;top:2706px;font-family:'Oswald',sans-serif;font-weight:600;font-size:30px;letter-spacing:.5px;color:#e8d6b0}
.footer-col{color:var(--white)}
.footer-head{font-family:'Oswald',sans-serif;font-size:21px;font-weight:500;text-transform:uppercase;color:var(--white);letter-spacing:-.3px}
.footer-links{list-style:none;font-size:14px;line-height:26.7px;margin-top:16px;color:var(--white)}
.footer-copy{font-size:14px;line-height:19px;margin-top:18px;width:236px;color:var(--white)}
.field{background:var(--footer-field);color:var(--white);font-size:14px;padding:14px 17px}
.send{left:794px;top:2700px;width:79px;height:39px;background:var(--white);color:var(--brown);font-weight:500;font-size:14px;display:flex;align-items:center;justify-content:center}
.footer-rule{left:89px;top:2805px;width:1022px;height:1px;background:rgba(255,255,255,.35)}
.copyright{left:0;top:2824px;width:1200px;text-align:center;font-family:'Oswald',sans-serif;font-size:15px;letter-spacing:-.3px;color:var(--white)}
.follow{right:86px;top:2823px;display:flex;align-items:center;gap:8px;font-size:14px;font-weight:500;color:var(--white)}
.follow i{width:24px;height:24px;border-radius:50%;background:#c13584;display:block}
.to-top{left:1140px;top:2786px;width:36px;height:36px;border-radius:50%;background:var(--white);display:flex;align-items:center;justify-content:center}
</style>
</head>
<body>

<header class="abs site-header">
  <div class="abs brand"><span class="brand-dot"></span>TRELMAVISTA</div>
  <nav class="abs nav"><span>HOME</span><span>SERVICE</span><span>HOW IT WORKS</span><span>WHY TRELMAVISTA</span><span>TEAM</span><span>BLOG</span><span>CONTACT US</span></nav>
</header>

<section class="abs hero"></section>
<h1 class="abs display hero-title">Personal<br>Trip Planning</h1>
<p class="abs hero-copy">Based on your needs, budget, and constraints, a Trelmavista travel engineer will work to create a tailored itinerary for you.</p>
<span class="abs btn hero-btn">GET STARTED</span>
<div class="abs hero-art" role="img" aria-label="Illustration of a family with suitcases in front of a beach scene with palm trees"></div>

<h2 class="abs display section-title" style="top:598px">How It Works</h2>

<div class="abs step left" style="left:109px;top:688px;width:310px">
  <div class="step-title">Share your preferences</div>
  <p class="step-copy">Connect with a Trelmavista Travel Engineer and discuss your expectations, needs, and budget.</p>
</div>
<div class="abs step-icon" style="left:431px;top:686px">
  <svg width="40" height="40" viewBox="0 0 40 40" fill="none" stroke="#4B3612" stroke-width="2"><circle cx="17" cy="17" r="7"/><path d="M17 4v4M17 26v4M4 17h4M26 17h4M8 8l3 3M23 23l3 3M26 8l-3 3M8 26l3-3"/><circle cx="29" cy="29" r="6"/></svg>
</div>
<div class="abs step left" style="left:139px;top:814px;width:280px">
  <div class="step-title">Let us do the work</div>
  <p class="step-copy">Our teams will be hard at work handcrafting plans, ahead of your next departure.</p>
</div>
<div class="abs step-icon" style="left:431px;top:812px">
  <svg width="40" height="40" viewBox="0 0 40 40" fill="none" stroke="#4B3612" stroke-width="2"><path d="M6 12l16 6 8-6 3 3-7 8 2 12-3 1-6-10-8 2-2-3 6-4z"/><circle cx="26" cy="26" r="7"/></svg>
</div>

<div class="abs mascot" role="img" aria-label="Brand mascot llama with sunglasses and a location pin"></div>

<div class="abs step-icon" style="left:697px;top:686px">
  <svg width="40" height="40" viewBox="0 0 40 40" fill="none" stroke="#4B3612" stroke-width="2"><path d="M12 34s-7-8-7-13a7 7 0 0114 0c0 5-7 13-7 13z"/><circle cx="12" cy="21" r="2.5"/><path d="M30 18s-5-6-5-9a5 5 0 0110 0c0 3-5 9-5 9z"/><path d="M18 32h6a4 4 0 000-8h-2" stroke-dasharray="3 3"/></svg>
</div>
<div class="abs step right" style="left:784px;top:688px;width:310px">
  <div class="step-title">Obtain your itinerary</div>
  <p class="step-copy">Access a personal, digital itinerary through your favorite devices.</p>
</div>
<div class="abs step-icon" style="left:697px;top:812px">
  <svg width="40" height="40" viewBox="0 0 40 40" fill="none" stroke="#4B3612" stroke-width="2"><circle cx="20" cy="22" r="12"/><path d="M17 6h6M20 6v4M23 17h-4a2.5 2.5 0 000 5h2a2.5 2.5 0 010 5h-4M20 14v3M20 27v3"/></svg>
</div>
<div class="abs step right" style="left:784px;top:814px;width:265px">
  <div class="step-title">Save time and money</div>
  <p class="step-copy">Avoid common mistakes and travel planning frustrations. We've got you covered.</p>
</div>

<div class="abs divider"></div>

<h2 class="abs display section-title" style="top:1064px">Our Pricing Plan</h2>

<article class="abs plan standard">
  <h3 class="display plan-name">Standard Trip Planning</h3>
  <div class="plan-price"><b>30 USD</b> / TRAVEL DAY</div>
  <ul class="plan-list">
    <li>Personalized, hand-crafted itinerary</li>
    <li>Unlimited chat with a travel engineer</li>
    <li>20-minute kick-off call with Trelmavista</li>
    <li>Lodging, food and entertainment recommendations</li>
    <li>Access to user-friendly, online itinerary tool</li>
    <li>Initial itinerary delivered in 2 weeks</li>
  </ul>
  <span class="btn plan-btn">GET STARTED</span>
</article>
<div class="abs plan-badge" style="left:303px;top:1150px" role="img" aria-label="Cartoon llama with sunglasses and a red scarf"></div>

<article class="abs plan premium">
  <h3 class="display plan-name">Premium Trip Planning</h3>
  <div class="plan-price"><b>60 USD</b> / TRAVEL DAY</div>
  <ul class="plan-list">
    <li class="lead">Standard Plan + the following premium services:</li>
    <li>Flight bookings</li>
    <li>Accommodation negotiation and reservations</li>
    <li>Restaurant and activity reservations</li>
    <li>Concierge service</li>
    <li>Traveler's itinerary booklet</li>
  </ul>
  <span class="btn plan-btn">GET STARTED</span>
</article>
<div class="abs plan-badge" style="left:759px;top:1150px" role="img" aria-label="Cartoon llama wearing a safari hat and scarf"></div>

<h2 class="abs display section-title" style="top:1774px;line-height:41px">Experiences curated with inspiration from<br>our brand ambassadors</h2>

<article class="abs ambassador" style="left:89px">
  <div class="ambassador-photo" style="background:linear-gradient(160deg,#b58a74,#6b4a3c)" role="img" aria-label="Portrait of a woman in a beret"></div>
  <div class="ambassador-name">Solenne Varrel</div>
  <div class="ambassador-role">French Lifestyle Influencer</div>
</article>
<article class="abs ambassador" style="left:350px">
  <div class="ambassador-photo" style="background:linear-gradient(160deg,#9a8a6a,#5a3e32)" role="img" aria-label="Portrait of a man in a top hat and checked jacket"></div>
  <div class="ambassador-name">Mathis Delorne</div>
  <div class="ambassador-role">Founder &amp; CEO</div>
</article>
<article class="abs ambassador" style="left:611px">
  <div class="ambassador-photo" style="background:linear-gradient(180deg,#4f8ccc,#a9c6e2 60%,#c8a878)" role="img" aria-label="Woman doing a yoga stretch in front of the pyramids"></div>
  <div class="ambassador-name">Nadia Elkarim</div>
  <div class="ambassador-role">Egyptologist</div>
</article>
<article class="abs ambassador" style="left:873px">
  <div class="ambassador-photo" style="top:0;background:linear-gradient(160deg,#6e8a4e,#3a4a2e)" role="img" aria-label="Man in a suit playing a double bass outdoors"></div>
  <div class="ambassador-name">Lorenzo Vitari</div>
  <div class="ambassador-role">Italian Singer</div>
</article>
<div class="abs dots"><span class="on"></span><span></span><span></span></div>

<footer class="abs site-footer"></footer>
<div class="abs footer-mark" role="img" aria-label="Brand mascot llama emblem"></div>
<div class="abs footer-brand">TRELMAVISTA</div>

<div class="abs footer-col" style="left:308px;top:2486px">
  <div class="footer-head">About Trelmavista</div>
  <ul class="footer-links">
    <li>› Personal Trip Planning</li>
    <li>› Business Trip Planning</li>
    <li>› Overseas Event Planning</li>
    <li>› Free Travel Resources</li>
    <li>› Terms and Conditions</li>
    <li>› Privacy Policy</li>
  </ul>
</div>
<div class="abs footer-col" style="left:528px;top:2486px">
  <div class="footer-head">Trelmavista</div>
  <p class="footer-copy">Trelmavista's mission is to engineer personalized, handcrafted travel itineraries and event plans for travelers worldwide.</p>
</div>
<div class="abs footer-col" style="left:794px;top:2486px">
  <div class="footer-head">Contact Us</div>
</div>
<div class="abs field" style="left:794px;top:2540px;width:155px;height:43px">Name</div>
<div class="abs field" style="left:955px;top:2540px;width:155px;height:43px">Email</div>
<div class="abs field" style="left:794px;top:2590px;width:316px;height:96px">Message</div>
<div class="abs send">SEND</div>

<div class="abs footer-rule"></div>
<div class="abs copyright">©TRELMAVISTA 2020. ALL RIGHTS RESERVED.</div>
<div class="abs follow"><i></i>Follow us on Picturely</div>
<div class="abs to-top">
  <svg width="14" height="14" viewBox="0 0 14 14" fill="none" stroke="#4B3612" stroke-width="1.5"><path d="M7 13V1M2 6l5-5 5 5"/></svg>
</div>

</body>
</html>
```